Silver Reed Harbour Seniors Fairway Festival 2107

I would like a design for an A4 Event Flyer.

This is a golf event for Senior ladies and gentlemen. I would like the design to appeal to an older age group.

I would like somewhere on the flyer a golf ball image with the following details inside "Please put me on your notice board"

The information on the Flyer is as follows
- (Title - Silver reed Harbour Seniors Fairway Festival 2017)
- Date 16th of October to 20th of October
- Over 55 years of age
- We invite our fellow Veteran Ladies and Gentlemen to play a unique 54 hole stableford event at three fantastic Golf Courses, and finish the week at Brindle Golf club with a 2BBB Medley.
- Insert schedule that is attached in PDF. They layout can be changed.

- For entry form and details
Contact: Brindle Proshop on 02 63918204 or email admin@brindlewexmoorgolf.com.au

I have attached 4 golf course images. This is a photo of each course. Could I please get these added to the flyer.

Target Market(s)

seniors

Industry/Entity Type

Golf Course

Requirements
Must have
• All information provided

```html
<!DOCTYPE html>
<html lang="en">
<head>
<meta charset="utf-8">
<title>Silver Reed Harbour Seniors Fairway Festival 2017 – Flyer</title>
<link href="https://fonts.googleapis.com/css2?family=Anton&family=Roboto+Condensed:wght@400;700&family=Barlow+Condensed:wght@500;600;700&family=Roboto:wght@400&family=Yesteryear&display=swap" rel="stylesheet">
<style>
  :root{
    --page:#ecebe8;
    --lime:#cfdc2b;
    --red:#e41e26;
    --blue:#0d4ea6;
    --green:#1f8a3a;
    --ink:#1d1d1d;
    --cream:#f3f0dc;
    --white:#ffffff;
  }
  *{margin:0;padding:0;box-sizing:border-box}
  html,body{width:1200px;height:1200px;overflow:hidden;background:var(--page)}
  .flyer{position:absolute;left:190px;top:20px;width:820px;height:1160px;overflow:hidden;background:var(--cream);box-shadow:0 4px 14px rgba(0,0,0,.18)}
  .layer{position:absolute;left:0;top:0}
  .hero-photo{position:absolute;left:0;top:0;width:820px;height:418px;
    background:linear-gradient(180deg,#4f86c9 0%,#9cc3e6 38%,#7fae4a 68%,#5d9a2e 100%)}
  .course-photo{position:absolute;left:274px;top:473px;width:546px;height:540px;
    background:linear-gradient(180deg,#9ec0d8 0%,#8fae6a 18%,#8fbf5a 32%,#c5d88f 62%,var(--cream) 100%)}
  .fairway-photo{position:absolute;left:0;top:1013px;width:820px;height:147px;
    background:linear-gradient(180deg,#2f6b25 0%,#5f9f3a 55%,#3c7a2a 100%)}
  .title{position:absolute;left:388px;top:22px;width:360px}
  .date-band{position:absolute;left:333px;top:418px;width:487px;height:55px;background:var(--lime)}
  .dates{position:absolute;left:0;top:0;width:487px;height:55px;line-height:55px;text-align:center;
    font-family:"Barlow Condensed",sans-serif;font-weight:600;font-size:42px;color:var(--blue)}
  .invite{position:absolute;left:20px;top:340px;width:300px;transform:rotate(-6deg);text-align:center;
    font-family:"Roboto Condensed",sans-serif;font-size:21px;line-height:27px;color:var(--blue)}
  .invite .script{font-family:"Yesteryear",cursive;font-size:50px;line-height:52px;color:var(--red);display:block}
  .invite strong{font-weight:700}
  .notice-text,.age-text,.entry-text{position:absolute;text-align:center}
  .notice-text{left:684px;top:90px;width:124px;transform:rotate(6deg);
    font-family:"Anton",sans-serif;font-size:17px;line-height:20px;color:var(--green);text-transform:uppercase}
  .age-text{left:30px;top:630px;width:160px;transform:rotate(-6deg);font-family:"Barlow Condensed",sans-serif;color:var(--green);font-weight:700;line-height:1}
  .age-text .over{font-size:40px;display:block}
  .age-text .num{font-size:64px;display:block;line-height:.9}
  .age-text .yrs{font-size:17px;display:block}
  .entry-text{left:28px;top:874px;width:300px;font-family:"Barlow Condensed",sans-serif;line-height:1}
  .entry-text .head{font-family:"Anton",sans-serif;color:var(--red);font-size:25px;line-height:27px;display:block}
  .entry-text .line{font-family:"Roboto Condensed",sans-serif;font-size:16px;line-height:21px;color:var(--ink);display:block}
  .entry-text .hl{color:var(--blue)}
  .program{position:absolute;left:362px;top:630px;width:450px;font-family:"Barlow Condensed",sans-serif;color:var(--ink)}
  .program h2{font-family:"Anton",sans-serif;font-weight:400;font-size:25px;color:var(--red);letter-spacing:.5px;margin-bottom:10px}
  .row{display:grid;grid-template-columns:92px 91px 1fr;font-size:16px;line-height:19px;margin-bottom:8px}
  .row .day{font-weight:700;font-size:16px}
  .row .date{font-weight:500}
  .row .venue{font-weight:700;font-size:19px;color:var(--blue)}
  .row .par{font-weight:500;font-size:16px;color:var(--ink)}
  .row .detail{font-weight:500}
  .row.leisure{color:var(--red);margin-bottom:4px}
  .row.leisure .day,.row.leisure .date{font-weight:600;color:var(--red)}
  .row.leisure .venue{color:var(--red)}
  .dinner{color:var(--red);font-weight:600}
</style>
</head>
<body>
<main class="flyer">
  <div class="hero-photo" role="img" aria-label="Photograph of a smiling senior golfing couple on a sunny course"></div>
  <div class="course-photo" role="img" aria-label="Photograph of a seaside golf course with palms and hills, fading into cream"></div>
  <div class="fairway-photo" role="img" aria-label="Aerial photograph of a tree-lined fairway"></div>

  <svg class="layer" width="820" height="1160" viewBox="0 0 820 1160" aria-hidden="true">
    <defs>
      <radialGradient id="ball" cx="40%" cy="35%" r="70%">
        <stop offset="0" stop-color="#ffffff"/>
        <stop offset=".65" stop-color="#e7e7e7"/>
        <stop offset="1" stop-color="#bdbdbd"/>
      </radialGradient>
    </defs>
    <!-- lime backdrop on left column -->
    <path d="M0 470 Q120 410 250 440 Q330 470 360 560 L330 1013 L0 1013 Z" fill="var(--lime)"/>
    <rect x="0" y="600" width="300" height="413" fill="var(--lime)"/>
    <circle cx="174" cy="950" r="168" fill="var(--lime)"/>
    <!-- invitation circle -->
    <circle cx="170" cy="470" r="166" fill="var(--white)"/>
    <!-- age ball -->
    <circle cx="108" cy="703" r="86" fill="var(--white)"/>
    <circle cx="108" cy="703" r="80" fill="url(#ball)"/>
    <!-- entry ball -->
    <circle cx="174" cy="950" r="150" fill="url(#ball)"/>
    <rect x="0" y="1013" width="820" height="1" fill="#2f6b25"/>
    <!-- right edge ball -->
    <circle cx="872" cy="612" r="124" fill="var(--lime)"/>
    <circle cx="872" cy="612" r="104" fill="url(#ball)"/>
    <!-- notice ball -->
    <circle cx="746" cy="142" r="70" fill="var(--white)"/>
    <circle cx="746" cy="142" r="64" fill="url(#ball)"/>
  </svg>

  <svg class="title" width="360" height="360" viewBox="0 0 360 360" role="img" aria-label="Silver Reed Harbour Seniors Fairway Festival 2017">
    <g font-family="Anton, sans-serif" font-size="56" text-anchor="middle" fill="var(--red)" stroke="var(--white)" stroke-width="5" paint-order="stroke" stroke-linejoin="round">
      <text x="180" y="56">SILVER REED</text>
      <text x="180" y="116">HARBOUR</text>
      <text x="180" y="178">SENIORS</text>
      <text x="180" y="239">FAIRWAY</text>
      <text x="180" y="299">FESTIVAL</text>
      <text x="180" y="358">2017</text>
    </g>
  </svg>

  <p class="notice-text">Please<br>put me on<br>your notice<br>board!</p>

  <div class="date-band"><p class="dates">16th October - 20th October</p></div>

  <p class="invite"><span class="script">We invite</span>our fellow Veteran Ladies and Gentlemen to play a unique <strong>54 hole stableford event</strong> at three fantastic Golf Courses, and finish the week at Brindle Golf club with a 2BBB Medley</p>

  <p class="age-text"><span class="over">OVER</span><span class="num">55</span><span class="yrs">YEARS OF AGE</span></p>

  <p class="entry-text"><span class="head">FOR ENTRY<br>FORM &amp; DETAILS</span><span class="line">Brindle Proshop on</span><span class="line"><span class="hl">02 63918204</span> or email</span><span class="line hl">admin@brindlewexmoorgolf.com.au</span></p>

  <section class="program">
    <h2>PROGRAM</h2>
    <div class="row"><span class="day">SUNDAY</span><span class="date">15 October</span><span><span class="venue">Brindle Golf Club</span><br><span class="detail">Registrations: 4.00pm - 6.00pm</span></span></div>
    <div class="row"><span class="day">MONDAY</span><span class="date">16 October</span><span><span class="venue">Wexmoor Golf Course</span> <span class="par">Par 72</span><br><span class="detail">Stableford - 1st Round Championships</span></span></div>
    <div class="row"><span class="day">TUESDAY</span><span class="date">17 October</span><span><span class="venue">Carrow Golf Course</span> <span class="par">Par 71</span><br><span class="detail">RHVGA Trophy Day Stableford - 2nd Round Championships</span></span></div>
    <div class="row leisure"><span class="day">WEDNESDAY</span><span class="date">18 October</span><span class="venue">LEISURE</span></div>
    <div class="row"><span class="day">THURSDAY</span><span class="date">19 October</span><span><span class="venue">Ashgrove Golf Course</span> <span class="par">Par 72</span><br><span class="detail">Stableford - Round 3 Championships</span></span></div>
    <div class="row"><span class="day">FRIDAY</span><span class="date">20 October</span><span><span class="venue">Brindle Golf Course</span> <span class="par">Par 66</span><br><span class="detail">18 Hole 2BBB Medley Stableford</span><br><span class="venue">Brindle Golf Club -</span><br><span class="dinner">PRESENTATION DINNER DANCE -<br>7.00pm for 7.30pm</span></span></div>
  </section>
</main>
</body>
</html>
```